Urgently Need UI designer for Mobile app

Need to design the following page

1. Welcome Screen
2. Login Page
3. User registration Page

Color Theme: Purple
Deadline: Today
For other details refer the attachment

```html
<!DOCTYPE html>
<html lang="en">
<head>
<meta charset="utf-8">
<title>Purple Learning App – Onboarding, Login and Sign up</title>
<link rel="stylesheet" href="https://fonts.googleapis.com/css2?family=Inter:wght@400;500;600;700;800&display=swap">
<style>
  :root {
    --canvas-bg: #d8c4dd;
    --brand: #5f1a6b;
    --brand-soft: #7b3a88;
    --illus-light: #b9a3e6;
    --illus-mid: #8c6fd0;
    --white: #ffffff;
    --ink: #1b1020;
    --muted: #7a6b7e;
    --field-border: #5f1a6b;
    --divider: #9a8f9c;
    --social-bg: #eeeeef;
  }
  * { box-sizing: border-box; margin: 0; padding: 0; }
  html, body {
    width: 1200px; height: 723px; overflow: hidden;
    background: var(--canvas-bg);
    font-family: "Inter", Arial, sans-serif;
  }
  .canvas { position: relative; width: 1200px; height: 723px; }

  .screen {
    position: absolute; top: 143px; width: 168px; height: 361px;
    border-radius: 16px; overflow: hidden;
  }
  .screen--onboarding { background: var(--brand); color: var(--white); }
  .screen--auth { background: var(--white); }

  .screen--admin   { left: 92px; }
  .screen--faculty { left: 313px; }
  .screen--learner { left: 516px; }
  .screen--login   { left: 720px; }
  .screen--signup  { left: 923px; }

  /* onboarding */
  .onboarding__art {
    position: absolute; left: 34px; top: 44px; width: 100px; height: 152px;
    border-radius: 50% 50% 46% 46%;
    background: radial-gradient(ellipse at 50% 70%, var(--illus-light) 0%, var(--illus-mid) 45%, rgba(95,26,107,0) 75%);
  }
  .onboarding__art--wide {
    left: 20px; top: 100px; width: 128px; height: 96px; border-radius: 14px;
    background: radial-gradient(ellipse at 50% 60%, var(--illus-light) 0%, var(--illus-mid) 45%, rgba(95,26,107,0) 78%);
  }
  .onboarding__caption {
    position: absolute; left: 28px; right: 12px; top: 219px;
    font-size: 9.5px; line-height: 1.2;
  }
  .screen--learner .onboarding__caption { left: 52px; top: 230px; }
  .onboarding__caption span { display: block; font-weight: 400; }
  .onboarding__caption strong { display: block; font-weight: 700; }

  .pager {
    position: absolute; left: 0; right: 0; top: 326px;
    display: flex; justify-content: center; gap: 7px;
  }
  .pager__dot { width: 7px; height: 7px; border-radius: 50%; background: var(--white); }
  .pager__dot--active { background: var(--ink); }

  /* auth header */
  .auth__header {
    position: absolute; left: 0; right: 0; top: 0; height: 145px;
    background: var(--brand);
  }
  .auth__art {
    position: absolute; top: 40px; width: 64px; height: 100px; border-radius: 10px;
    background: linear-gradient(180deg, #f4eef6 0%, #d9cde0 100%);
  }
  .screen--login .auth__art { left: 38px; }
  .screen--signup .auth__art { left: 44px; top: 56px; width: 54px; height: 80px; }

  .auth__title {
    position: absolute; left: 16px; top: 155px;
    font-size: 14px; font-weight: 700; color: var(--ink);
  }
  .screen--signup .auth__title { color: var(--brand); }

  .field {
    position: absolute; left: 18px; width: 130px; height: 18px;
    border: 1.3px solid var(--field-border); border-radius: 3px;
    display: flex; align-items: center; justify-content: space-between;
    padding: 0 5px 0 14px;
    font-size: 7.5px; color: var(--muted); font-weight: 500;
  }
  .field svg { width: 10px; height: 10px; fill: var(--brand); }
  .screen--signup .field { padding-left: 9px; color: #9b8f9f; font-weight: 400; }

  .btn {
    position: absolute; left: 18px; width: 130px; height: 19px; border-radius: 3px;
    background: var(--brand); color: var(--white);
    font-size: 8px; font-weight: 700;
    display: flex; align-items: center; justify-content: center;
  }

  .link-forgot {
    position: absolute; right: 20px; top: 238px;
    font-size: 5.5px; font-weight: 600; color: var(--ink);
  }
  .auth__switch {
    position: absolute; left: 0; right: 0; top: 285px; text-align: center;
    font-size: 5.5px; color: var(--muted);
  }
  .auth__switch b { color: var(--ink); font-weight: 700; }
  .auth__divider {
    position: absolute; left: 18px; right: 18px; top: 305px;
    display: flex; align-items: center; gap: 5px;
    font-size: 5.5px; color: var(--ink);
  }
  .auth__divider::before, .auth__divider::after {
    content: ""; flex: 1; height: 1px; background: var(--divider);
  }
  .social {
    position: absolute; left: 0; right: 0; top: 320px;
    display: flex; justify-content: center; gap: 13px;
  }
  .social__item {
    width: 19px; height: 19px; border-radius: 50%; background: var(--social-bg);
    display: flex; align-items: center; justify-content: center;
    font-size: 3.6px; font-weight: 700; color: var(--brand);
  }
</style>
</head>
<body>
<main class="canvas">

  <section class="screen screen--onboarding screen--admin">
    <div class="onboarding__art" role="img" aria-label="Illustration of an administrator at a desk with connected user avatars"></div>
    <p class="onboarding__caption"><span>For Administrators...</span><strong>Interface with LEARNORA as a Local Chapter</strong></p>
    <div class="pager"><i class="pager__dot pager__dot--active"></i><i class="pager__dot"></i><i class="pager__dot"></i></div>
  </section>

  <section class="screen screen--onboarding screen--faculty">
    <div class="onboarding__art" role="img" aria-label="Illustration of a faculty member at a desk with connected student avatars"></div>
    <p class="onboarding__caption"><span>For Faculty...</span><strong>Faculty Development and Student Mentoring</strong></p>
    <div class="pager"><i class="pager__dot"></i><i class="pager__dot pager__dot--active"></i><i class="pager__dot"></i></div>
  </section>

  <section class="screen screen--onboarding screen--learner">
    <div class="onboarding__art onboarding__art--wide" role="img" aria-label="Illustration of learners around a large laptop with chat bubbles"></div>
    <p class="onboarding__caption"><span>For Learners...</span><strong>Acquire skills that meet your needs</strong></p>
    <div class="pager"><i class="pager__dot"></i><i class="pager__dot"></i><i class="pager__dot pager__dot--active"></i></div>
  </section>

  <section class="screen screen--auth screen--login">
    <div class="auth__header"><div class="auth__art" role="img" aria-label="Illustration of a person beside a large phone showing a login form"></div></div>
    <h2 class="auth__title">Login</h2>
    <div class="field" style="top:181px">Email
      <svg viewBox="0 0 10 10"><path d="M0 2h10v6H0z"/><path d="M0 2l5 3.5L10 2" fill="none" stroke="#fff" stroke-width="0.9"/></svg></div>
    <div class="field" style="top:213px">Password
      <svg viewBox="0 0 10 10"><rect x="0.5" y="1.5" width="9" height="2" rx="0.5"/><path d="M1 6c2 2.5 6 2.5 8 0" fill="none" stroke="#5f1a6b" stroke-width="1.3"/></svg></div>
    <span class="link-forgot">Forgot Password ?</span>
    <div class="btn" style="top:244px">Login</div>
    <p class="auth__switch">Dont have an Account? <b>Sign up</b></p>
    <p class="auth__divider">or Login with</p>
    <div class="social"><span class="social__item">Nimbus</span><span class="social__item">Orbit</span></div>
  </section>

  <section class="screen screen--auth screen--signup">
    <div class="auth__header"><div class="auth__art" role="img" aria-label="Illustration of a person beside a large phone with plants"></div></div>
    <h2 class="auth__title">Sign up</h2>
    <div class="field" style="top:180px">Name
      <svg viewBox="0 0 10 10"><circle cx="5" cy="5" r="5"/><circle cx="5" cy="3.8" r="1.7" fill="#fff"/><path d="M2 8.3c1.5-2 4.5-2 6 0" fill="#fff"/></svg></div>
    <div class="field" style="top:212px">Email
      <svg viewBox="0 0 10 10"><path d="M0 2h10v6H0z"/><path d="M0 2l5 3.5L10 2" fill="none" stroke="#fff" stroke-width="0.9"/></svg></div>
    <div class="field" style="top:246px">Password
      <svg viewBox="0 0 10 10"><rect x="0.5" y="1.5" width="9" height="2" rx="0.5"/><path d="M1 6c2 2.5 6 2.5 8 0" fill="none" stroke="#5f1a6b" stroke-width="1.3"/></svg></div>
    <div class="field" style="top:278px">Conform Password
      <svg viewBox="0 0 10 10"><rect x="0.5" y="1.5" width="9" height="2" rx="0.5"/><path d="M1 6c2 2.5 6 2.5 8 0" fill="none" stroke="#5f1a6b" stroke-width="1.3"/></svg></div>
    <div class="btn" style="top:314px">Signup</div>
  </section>

</main>
</body>
</html>
```